Halvik Denatl Laboratory nees a window design

We want to make a window cover 8 feet wide and 6 feet tall to advertise our dental lab with all the products we produce<br/>: Digital Cad/Cam<br/>: Implants<br/>: Dentures<br/>: Cast Partials <br/>: Orthodontic appliances<br/><br/> and it has to include a service we provide for a denturist on site by appointment only.<br/><br/>Please use the sample logo below our colours are white backround and blue letters

Font styles to use
Script

Colors
ffffff
0355a3

Requirements
Nice to have
• a picture of a teddy bear on a dental chair, or some dental work particularly bridge work since our moto is Building bridges since 1976
Should not have
• real people

```html
<!DOCTYPE html>
<html lang="en">
<head>
<meta charset="utf-8">
<title>Halvik Denatl Laboratory – Window Design</title>
<link href="https://fonts.googleapis.com/css2?family=EB+Garamond:wght@400&family=Open+Sans:wght@400;600;700&display=swap" rel="stylesheet">
<style>
  :root {
    --page-bg: #b3b3b3;
    --white: #ffffff;
    --brand-blue: #0355a3;
    --deep-blue: #0a3f86;
    --bright-blue: #1a67bf;
    --pill-blue: #3b82cc;
    --ink: #1b1b1b;
    --ghost-blue: #e9f0f9;
  }
  * { box-sizing: border-box; margin: 0; padding: 0; }
  html, body {
    width: 1200px; height: 1200px; overflow: hidden;
    background: var(--page-bg);
  }
  .window-cover {
    position: absolute; left: 40px; top: 182px;
    width: 1120px; height: 836px;
    background: var(--white);
    overflow: hidden;
  }
  .cover-shapes { position: absolute; inset: 0; }
  .headline {
    position: absolute; left: 74px; top: 44px;
    font-family: "EB Garamond", Georgia, serif;
    font-weight: 400; font-size: 106px; line-height: 120px;
    color: var(--brand-blue);
  }
  .headline-rule {
    position: absolute; left: 72px; top: 410px;
    width: 516px; height: 5px; background: var(--brand-blue);
  }
  .side-tab {
    position: absolute; left: 0; top: 455px;
    width: 17px; height: 76px; background: var(--brand-blue);
  }
  .tagline {
    position: absolute; left: 72px; top: 450px;
    font-family: "Open Sans", Arial, sans-serif;
    font-size: 26px; line-height: 38px; color: var(--ink);
  }
  .brand-name {
    position: absolute; left: 740px; top: 66px; width: 320px;
    font-family: "EB Garamond", Georgia, serif;
    font-weight: 400; font-size: 40px; line-height: 44px;
    color: var(--brand-blue); text-align: center;
  }
  .services {
    position: absolute; right: 28px; top: 318px; width: 430px;
    font-family: "Open Sans", Arial, sans-serif;
    font-size: 17px; line-height: 25px; text-align: right;
    color: var(--ink);
  }
  .services .denturist { color: var(--brand-blue); font-weight: 700; }
  .helpline {
    position: absolute; left: 72px; top: 596px;
    width: 433px; height: 93px; border-radius: 47px;
    background: var(--pill-blue);
    display: flex; align-items: center; padding-left: 44px;
    color: var(--white); font-family: "Open Sans", Arial, sans-serif;
  }
  .helpline-icon { width: 54px; height: 54px; margin-right: 26px; }
  .helpline-label { font-size: 24px; font-weight: 600; line-height: 30px; }
  .helpline-number { font-size: 41px; font-weight: 700; line-height: 46px; letter-spacing: 0.5px; }
  .website {
    position: absolute; left: 72px; top: 766px;
    display: flex; align-items: center;
    font-family: "Open Sans", Arial, sans-serif;
    font-size: 24px; letter-spacing: 5px; color: var(--ink);
  }
  .website svg { width: 24px; height: 24px; margin-right: 22px; }
  .website strong { color: var(--brand-blue); font-weight: 700; }
</style>
</head>
<body>
  <main class="window-cover">
    <svg class="cover-shapes" viewBox="0 0 1120 836" width="1120" height="836">
      <defs>
        <linearGradient id="photoTone" x1="0" y1="0" x2="1" y2="1">
          <stop offset="0" stop-color="#7d9bd8"/>
          <stop offset="0.5" stop-color="#c9b68e"/>
          <stop offset="1" stop-color="#9fb6e6"/>
        </linearGradient>
      </defs>
      <ellipse class="implant-sketch" role="img" aria-label="Faint dental implant line drawing" cx="292" cy="290" rx="105" ry="250" fill="var(--ghost-blue)" opacity="0.7"/>
      <rect class="contact-band" x="0" y="566" width="1120" height="151" fill="var(--brand-blue)"/>
      <path class="swoosh-back" d="M416 0 C520 150 640 280 760 292 C900 300 1040 200 1120 135 L1120 150 C1040 230 900 330 760 322 C620 310 500 170 400 0 Z" fill="var(--deep-blue)"/>
      <path class="swoosh-mid" d="M440 0 C540 140 650 255 765 262 C900 270 1040 180 1120 128 L1120 140 C1040 200 900 292 762 288 C630 280 520 150 416 0 Z" fill="var(--brand-blue)"/>
      <path class="swoosh-front" d="M480 0 C570 120 670 225 770 232 C900 240 1040 165 1120 122 L1120 132 C1040 185 900 265 765 262 C650 255 540 140 440 0 Z" fill="var(--bright-blue)"/>
      <path class="photo-frame" role="img" aria-label="Photo of a teddy bear resting in a dental chair"
        d="M605 560 Q600 440 720 425 Q1000 410 1040 520 Q1050 600 960 700 Q880 800 800 790 Q700 770 640 680 Q608 630 605 560 Z"
        fill="url(#photoTone)" stroke="var(--bright-blue)" stroke-width="6"/>
    </svg>

    <h1 class="headline">Your<br>Health Is<br>Our Priority</h1>
    <div class="headline-rule"></div>
    <div class="side-tab"></div>
    <p class="tagline">We offer the best healthcare for you an<br>your family with 100% Satisfaction</p>

    <div class="brand-name">Halvik Denatl<br>Laboratory</div>

    <div class="services">
      <p>Digital CAD/CAM · Implants · Dentures</p>
      <p>Cast Partials · Orthodontic Appliances</p>
      <p class="denturist">Denturist on site – by appointment only</p>
    </div>

    <div class="helpline">
      <svg class="helpline-icon" viewBox="0 0 24 24" fill="none" stroke="#ffffff" stroke-width="1.8" stroke-linecap="round">
        <path d="M6.6 3.5l2.3 3.6-1.6 2a12 12 0 0 0 7.6 7.6l2-1.6 3.6 2.3-1.3 3a3 3 0 0 1-3 1.2C9.6 20.6 3.4 14.4 2.4 8.8a3 3 0 0 1 1.2-3z" fill="#ffffff"/>
        <path d="M14 5.5a5 5 0 0 1 4.5 4.5"/>
        <path d="M14 2a8.5 8.5 0 0 1 8 8"/>
      </svg>
      <div>
        <div class="helpline-label">Emergancy Helpline</div>
        <div class="helpline-number">0123987654</div>
      </div>
    </div>

    <div class="website">
      <svg viewBox="0 0 24 24" fill="none" stroke="var(--deep-blue)" stroke-width="2">
        <circle cx="12" cy="12" r="10"/>
        <path d="M2 12h20M12 2c3 3 3 17 0 20M12 2c-3 3-3 17 0 20"/>
      </svg>
      <span>www.<strong>halviklab</strong>.com</span>
    </div>
  </main>
</body>
</html>
```